Harborline Energy - needs a business card

Harborline Energy is a U.S. based diesel sourcing and distribution company that supports American oil & gas fields through providing quality product and consistent services.

Target Market(s)

Oil and Gas

Contact Information for Business Card

The background of the card must be white to ensure the logo pops.

Font styles to use
Serif
Sans Serif

Colors

Designer to choose colors to be used in the design.

Requirements
Must have
• Front of Card: Tag line: Harborline Energy, Powering America's Oil & Gas fields.
• Not sure if you guys do this part but just in case...
• Dale Menschow
• Owner/CEO
• C:555.318.4076
• E:Dmenschow@harborlineenergy.example
• W:Harborlineenergy.example
• Locations: Servicing the Powder River, DJ basin and Bakken formations.
• Back of Card: " Frac fueling is what we do. We understand how important diesel fuel is to your operation, which is why our main service line is Frac fueling. We assure our supply and stand by our service"

```html
<!DOCTYPE html>
<html lang="en">
<head>
<meta charset="utf-8">
<title>Harborline Energy – Business Card</title>
<link rel="stylesheet" href="https://fonts.googleapis.com/css2?family=Lato:wght@400;700;900&display=swap">
<style>
  :root {
    --stage: #585858;
    --card-white: #ffffff;
    --navy: #13305f;
    --navy-deep: #0e2656;
    --red: #b3121a;
    --red-deep: #8e1420;
    --ink: #333333;
    --muted: #555555;
    --rule: rgba(255,255,255,0.55);
  }
  * { margin: 0; padding: 0; box-sizing: border-box; }
  html, body { width: 1200px; height: 900px; overflow: hidden; }
  body {
    background: var(--stage);
    font-family: "Lato", Arial, sans-serif;
    position: relative;
  }
  .card {
    position: absolute;
    top: 200px;
    width: 310px;
    height: 502px;
    overflow: hidden;
    box-shadow: 4px 5px 8px rgba(0,0,0,0.35);
  }
  .card-front {
    left: 253px;
    background: var(--card-white);
    border-radius: 52px 0 52px 0;
  }
  .card-back {
    left: 627px;
    border-radius: 0 52px 0 52px;
    background: linear-gradient(180deg, var(--red) 0%, var(--red-deep) 30%, #4a1f45 58%, var(--navy-deep) 85%, var(--navy) 100%);
  }
  .back-curves { position: absolute; inset: 0; }

  .brand-name {
    position: absolute;
    left: 0; right: 0;
    top: 120px;
    text-align: center;
    color: var(--navy);
    font-weight: 900;
    font-size: 30px;
    line-height: 1.1;
    letter-spacing: 0.5px;
  }

  .contact { position: absolute; left: 34px; top: 320px; right: 14px; }
  .person-name {
    font-size: 19px;
    font-weight: 700;
    color: var(--navy);
    line-height: 20px;
    letter-spacing: 0.3px;
  }
  .person-name .surname { color: var(--red); }
  .person-role { font-size: 14px; color: var(--muted); line-height: 17px; }
  .contact-list { list-style: none; margin-top: 9px; }
  .contact-list li {
    font-size: 13.5px;
    color: var(--ink);
    line-height: 18px;
    display: flex;
    align-items: center;
    gap: 4px;
    white-space: nowrap;
  }
  .contact-list svg { width: 12px; height: 12px; flex: none; fill: var(--navy); }
  .locations { margin-top: 8px; font-size: 14px; line-height: 18px; color: var(--ink); }
  .locations .label { color: var(--red); }

  .back-brand {
    position: absolute;
    left: 0; right: 0;
    top: 152px;
    text-align: center;
    color: #ffffff;
    font-weight: 900;
    font-size: 27px;
    letter-spacing: 1px;
  }
  .back-copy {
    position: absolute;
    left: 29px;
    top: 260px;
    width: 272px;
    color: #ffffff;
    font-size: 16px;
    line-height: 20px;
  }
  .back-rule {
    position: absolute;
    left: 29px;
    top: 391px;
    width: 256px;
    height: 1px;
    background: var(--rule);
  }
  .back-tagline {
    position: absolute;
    left: 33px;
    top: 412px;
    color: #ffffff;
    font-size: 16px;
    line-height: 21px;
    text-transform: uppercase;
  }
</style>
</head>
<body>
  <section class="card card-front" aria-label="Business card front">
    <div class="brand-name">Harborline<br>Energy</div>
    <div class="contact">
      <h1 class="person-name">DALE <span class="surname">MENSCHOW</span></h1>
      <p class="person-role">Owner/CEO</p>
      <ul class="contact-list">
        <li><svg viewBox="0 0 12 12" aria-hidden="true"><path d="M1 4c0-2 2-3 5-3s5 1 5 3l-2 1-1-2H4L3 5zM2 6h8l1 5H1z"/></svg>555.318.4076</li>
        <li><svg viewBox="0 0 12 12" aria-hidden="true"><path d="M1 3h10v7H1z M1 3l5 4 5-4" fill="none" stroke="#13305f" stroke-width="1.3"/></svg>Dmenschow@harborlineenergy.example</li>
        <li><svg viewBox="0 0 12 12" aria-hidden="true"><circle cx="6" cy="6" r="5.5"/></svg>www.Harborlineenergy.example</li>
      </ul>
      <p class="locations"><span class="label">Locations:</span> Servicing the Powder River DJ basin and Bakken formations.</p>
    </div>
  </section>

  <section class="card card-back" aria-label="Business card back">
    <svg class="back-curves" viewBox="0 0 310 502" aria-hidden="true">
      <path d="M230 0 C320 60 300 220 310 260 L310 0 Z" fill="rgba(255,255,255,0.05)"/>
      <path d="M0 300 C80 200 220 180 310 220 L310 300 C220 260 90 280 0 360 Z" fill="rgba(255,255,255,0.04)"/>
      <path d="M200 502 C230 440 280 420 310 440 L310 502 Z" fill="rgba(0,0,0,0.12)"/>
    </svg>
    <div class="back-brand">HARBORLINE ENERGY</div>
    <p class="back-copy">Frac fueling is what we do. We understand how important diesel fuel is to your operation which is why our main service line is Frac fueling. We assure our supply and stand by our service</p>
    <div class="back-rule"></div>
    <p class="back-tagline">Harborline Energy, Powering<br>America's Oil &amp; Gas fields.</p>
  </section>
</body>
</html>
```